#1 Selling Sweden weight loss supplement comes to USA - LABEL needed!

The number one weight loss in Sweden is coming to USA

-I need a label that is clean and simple but somehow represents, in an abstract way, weight loss or slender.
-The product and water mixed is all the is needed. This too could be represented in the label design.
-The bottle will be white.

-Attached is a picture of a supplement bottle with
--the logo for the company, 'NuKelvara'
--the name of the supplement, 'Kelvara Lithe'
and
--other text that could be included in the final label.

ALSO attached are 2 label designs that I like. This might give you an idea of a direction to go.
Thank You very much.

Target Market(s)

Health conscience people

Industry/Entity Type

Weight

Font styles to use
Sans Serif

Requirements
Must have
• -Size of bottle - 2" wide x 4" high
Nice to have
• *Lowers Hunger up to 50%
• *Decreases cravings or unhealthy foods up to 90%
• *Enhances Weight Loss
• " A Durovix a day keeps hunger away"

```html
<!DOCTYPE html>
<html lang="en">
<head>
<meta charset="utf-8">
<title>NuKelvara – Kelvara Lithe Label</title>
<link rel="stylesheet" href="https://fonts.googleapis.com/css2?family=Roboto:ital,wght@0,300;0,400;1,300&display=swap">
<style>
  :root {
    --navy: #1c2070;
    --title-blue: #23307f;
    --product-blue: #2160c4;
    --claim-blue: #2a5fb8;
    --brown: #5a3a18;
    --leaf-green: #27a84a;
    --tick-green: #2fb04f;
    --paper: #ffffff;
  }
  * { margin: 0; padding: 0; box-sizing: border-box; }
  html, body { width: 1200px; height: 900px; overflow: hidden; background: var(--paper); }
  body { font-family: "Roboto", "Helvetica Neue", Arial, sans-serif; font-weight: 300; }
  .canvas { position: relative; width: 1200px; height: 900px; }
  .label { position: absolute; top: 0; }
  .label > * { position: absolute; }

  .wordmark { color: var(--navy); font-weight: 300; white-space: nowrap; display: flex; align-items: center; line-height: 1; }
  .wordmark-dot { border-radius: 50%; background: var(--leaf-green); margin-left: 10px; flex: none; }

  .name-line { color: var(--title-blue); font-weight: 300; font-size: inherit; line-height: 1; white-space: nowrap; }
  .product { color: var(--product-blue); line-height: 1; white-space: nowrap; }
  .product sup { font-size: 0.45em; vertical-align: 1.1em; }

  .tagline { color: var(--brown); font-style: italic; white-space: nowrap; }

  .claims { list-style: none; left: 0; top: 0; width: 100%; height: 100%; }
  .claim { position: absolute; display: block; color: var(--claim-blue); white-space: nowrap; }
  .tick { position: absolute; fill: none; stroke: var(--tick-green); stroke-linecap: round; stroke-linejoin: round; }

  /* Large label */
  .label--large { left: 0; width: 600px; height: 900px; }
  .label--large .wordmark { left: 165px; top: 90px; font-size: 72px; }
  .label--large .wordmark-dot { width: 34px; height: 34px; }
  .label--large .name-first { left: 141px; top: 232px; font-size: 41px; }
  .label--large .name-second { left: 173px; top: 285px; font-size: 41px; }
  .label--large .product { left: 141px; top: 337px; font-size: 36px; }
  .label--large .hero { left: 300px; top: 275px; }
  .label--large .tagline { left: 140px; top: 562px; font-size: 26px; line-height: 46px; }
  .label--large .claim { left: 202px; font-size: 20px; line-height: 28px; }
  .label--large .tick { stroke-width: 3; }

  /* Small label */
  .label--small { left: 840px; width: 360px; height: 900px; }
  .label--small .wordmark { left: 25px; top: 68px; font-size: 40px; }
  .label--small .wordmark-dot { width: 20px; height: 20px; margin-left: 6px; }
  .label--small .name-first { left: 36px; top: 180px; font-size: 33px; }
  .label--small .name-second { left: 42px; top: 223px; font-size: 33px; }
  .label--small .product { left: 107px; top: 274px; font-size: 25px; }
  .label--small .hero { left: 13px; top: 305px; }
  .label--small .tagline { left: 48px; top: 574px; font-size: 26px; line-height: 44px; }
  .label--small .claim { left: 40px; width: 189px; text-align: right; font-size: 14.5px; line-height: 22px; }
  .label--small .tick { stroke-width: 2.4; }
</style>
</head>
<body>
<main class="canvas">

  <section class="label label--large" aria-label="Kelvara Lithe label, tall layout">
    <div class="wordmark">NuKelvara<span class="wordmark-dot"></span></div>
    <h1 class="name-line name-first">Kelvara</h1>
    <p class="name-line name-second">Lithe</p>
    <p class="product">Durovix<sup>®</sup></p>

    <svg class="hero" width="268" height="334" viewBox="0 0 268 334" role="img" aria-label="White spinach leaf bunch on a green circle">
      <circle cx="167" cy="167" r="166" fill="var(--leaf-green)"/>
    </svg>

    <p class="tagline">A Durovix<br>a day keeps hunger away</p>

    <ul class="claims">
      <li class="claim" style="top:686px">Lowers Hunger up to 50%</li>
      <li class="claim" style="top:743px">Decreases cravings or unhealthy foods<br>up to 90%</li>
      <li class="claim" style="top:828px">Enhances Weight Loss</li>
    </ul>
    <svg class="tick" style="left:160px;top:688px" width="34" height="30" viewBox="0 0 34 30"><path d="M3 17 L12 26 L31 3"/></svg>
    <svg class="tick" style="left:160px;top:752px" width="34" height="30" viewBox="0 0 34 30"><path d="M3 17 L12 26 L31 3"/></svg>
    <svg class="tick" style="left:160px;top:830px" width="34" height="30" viewBox="0 0 34 30"><path d="M3 17 L12 26 L31 3"/></svg>
  </section>

  <section class="label label--small" aria-label="Kelvara Lithe label, narrow layout">
    <div class="wordmark">NuKelvara<span class="wordmark-dot"></span></div>
    <p class="name-line name-first">Kelvara</p>
    <p class="name-line name-second">Lithe</p>
    <p class="product">Durovix<sup>®</sup></p>

    <svg class="hero" width="190" height="255" viewBox="0 0 190 255" role="img" aria-label="White spinach leaf bunch on a green circle">
      <circle cx="63" cy="128" r="125" fill="var(--leaf-green)"/>
    </svg>

    <p class="tagline">A Durovix<br>a day keeps<br>hunger away</p>

    <ul class="claims">
      <li class="claim" style="top:744px">Lowers Hunger up to 50%</li>
      <li class="claim" style="top:789px">Decreases cravings or<br>unhealthy foods up to 90%</li>
      <li class="claim" style="top:854px">Enhances Weight Loss</li>
    </ul>
    <svg class="tick" style="left:35px;top:742px" width="24" height="22" viewBox="0 0 24 22"><path d="M2 12 L8 19 L22 2"/></svg>
    <svg class="tick" style="left:35px;top:794px" width="24" height="22" viewBox="0 0 24 22"><path d="M2 12 L8 19 L22 2"/></svg>
    <svg class="tick" style="left:35px;top:853px" width="24" height="22" viewBox="0 0 24 22"><path d="M2 12 L8 19 L22 2"/></svg>
  </section>

</main>
</body>
</html>
```